Graphic Design Banners for my newsletters: Thermomugs

We sell merchandise to business costumers. We will send newsletters every week, and I need to find someone who can make me nice banners to my newsletters.The goal with my newsletters is to SELL the products and introduce costumers to my website: www.brevaloft.dk. I need 3 banners to my newsletters about thermomugs:* Banner 1 - Model 37205. I think an orange round price splash (69,- v/100 stk) with this text: "Drypfri og dobbeltvægget Termokrus i rustfri stål ude og PP inde med push funktion i lækkert design."* Banner 2 - Model 81362. I think an orange round price splash (49,- v/100 stk) with this text: "Dobbeltvægget Termokrus i PP plastik i 4 forskellige farver."* Banner 3 - KT4137. Bubble price splash (45,- v/100 stk) and this text: "Dobbeltvægget termokrus med hank. Rustfri stål ude og PP inde."Maybe it will be nice if it has a "call to action" BESTIL HER (in English, it means ORDER HERE) on each banner. Here, I've attached pictures for all 3 thermomugs. The filename is the modelnumber and I sent you pictures of how it appears right now in our newsletters, and I need you to make them nicer. Personally, I like the "Q&Z better than the other we made." but I need help, since it looks bad and unprofessional.Thank you.

Target Market(s)

Big and middle Big companies.

Industry/Entity Type

Promotional Merchandise

Colors
faa54b

Requirements
Must have
• I sent the newletters to marketing bosses so they like Nice style and proffesionalisme. They buy my products with there logo printed on. So the product details (Nice pictures) is importent to be in focus.
Nice to have
• I have sent some banners i use on my website. I like that style. But This to newletters Could be more kvadrat.

```html
<!DOCTYPE html>
<html lang="da">
<head>
<meta charset="utf-8">
<title>Termokrus – nyhedsbrev banner</title>
<link rel="stylesheet" href="https://fonts.googleapis.com/css2?family=Roboto:wght@400;700&family=Roboto+Condensed:wght@700&display=swap">
<style>
  :root {
    --paper: #ffffff;
    --ink: #111111;
    --frame: #1a1a1a;
    --orange: #f5922a;
    --product-light: #f4f4f4;
    --product-mid: #d9d9d9;
  }
  html, body {
    margin: 0;
    padding: 0;
    width: 1200px;
    height: 600px;
    overflow: hidden;
    background: var(--paper);
  }
  .banner {
    position: relative;
    width: 1200px;
    height: 600px;
    background: var(--paper);
    font-family: "Roboto", Arial, sans-serif;
    color: var(--ink);
  }
  .banner__frame {
    position: absolute;
    left: 30px;
    top: 22px;
    width: 1142px;
    height: 554px;
    border: 3px solid var(--frame);
    box-sizing: border-box;
  }
  .product-visual {
    position: absolute;
    left: 72px;
    top: 80px;
    width: 640px;
    height: 322px;
    border-radius: 6px;
    background: linear-gradient(180deg, var(--product-light) 0%, var(--product-mid) 100%);
  }
  .price-splash {
    position: absolute;
    left: 790px;
    top: 0;
    width: 330px;
    height: 290px;
  }
  .price-splash__label {
    position: absolute;
    left: 835px;
    top: 70px;
    width: 240px;
    text-align: center;
    color: var(--paper);
    transform: rotate(-16deg);
    font-weight: 700;
  }
  .price-splash__amount {
    display: block;
    font-size: 76px;
    line-height: 1;
    letter-spacing: 1px;
  }
  .price-splash__unit {
    display: block;
    font-family: "Roboto", Arial, sans-serif;
    font-weight: 400;
    font-size: 30px;
    margin-top: 4px;
  }
  .product-copy {
    position: absolute;
    left: 78px;
    top: 412px;
    margin: 0;
    font-size: 26px;
    line-height: 42px;
    font-weight: 400;
  }
  .order-cta {
    position: absolute;
    left: 642px;
    top: 488px;
    width: 528px;
    height: 84px;
    display: flex;
    align-items: center;
    justify-content: flex-end;
    padding-right: 36px;
    box-sizing: border-box;
    background: var(--orange);
    clip-path: polygon(60px 0, 100% 0, 100% 100%, 0 100%);
    font-family: "Roboto Condensed", "Arial Narrow", sans-serif;
    font-weight: 700;
    font-size: 29px;
    color: var(--ink);
    text-decoration: none;
    letter-spacing: 0.2px;
  }
</style>
</head>
<body>
  <main class="banner">
    <div class="banner__frame"></div>

    <div class="product-visual" role="img" aria-label="Termokrus i hvid og sort rustfri stål med låg, vist stående, liggende og med låget skruet af"></div>

    <svg class="price-splash" viewBox="0 0 330 290" aria-hidden="true">
      <circle cx="158" cy="132" r="122" fill="var(--orange)"/>
    </svg>
    <div class="price-splash__label">
      <span class="price-splash__amount">69,-</span>
      <span class="price-splash__unit">v/100 stk</span>
    </div>

    <p class="product-copy">
      Drypfri og dobbeltvægget<br>
      Termokrus i rustfri stål ude og PP<br>
      inde med push funktion i lækkert design.
    </p>

    <a class="order-cta" href="#">BESTIL OG SE MERE HER</a>
  </main>
</body>
</html>
```